Redesign Logo Business Cards and Stationary
Brivosa
Redesign Logo Business Cards and Stationary - Construction
Creative Brief
Construction Services Group
Yes
This logo will reflect our company's credibility as a proffesional in the Multi-Family Renovation Industry. http://www.brivosagroup.example/
Professional
Please keep the current color from our existing logo and web site. www.BrivosaGroup.example
Make sure you look at the current business card files attached and the business card examples attached to this project.
I will need cards as follows
Backside of card:
Our Services:
Interior Renovations
Exterior Painting & Carpentry
Concrete Work
Siding Installation
Step Tread Replacements
Front side:
Derek J. Whitcombe
President
Phone: 615-555-0182 Fax 866-555-0147
Email: Dwhitcombe@BrivosaGroup.example
1873-K Hollis Bend Rd. #529
Murfreesboro, TN 37190
www.BrivosaGroup.example
Rolf Tenneker
Vice-President
Phone: 404-555-0139 Fax 866-555-0147
Email: RTenneker@BrivosaGroup.example
Front:
Gideon Hulme
Administrative Manager
Phone: 615-555-0164 Fax 866-555-0147
Email: GHulme@BrivosaGroup.example
Oskar Dähn
Project Manager
Phone: 615-555-0121 Fax 866-555-0147
Email: ODahn@BrivosaGroup.example

```html
<!DOCTYPE html>
<html lang="en">
<head>
<meta charset="utf-8">
<title>Brivosa Stationery</title>
<link href="https://fonts.googleapis.com/css2?family=Montserrat:wght@700&family=Open+Sans:wght@400;600;700&display=swap" rel="stylesheet">
<style>
  :root {
    --canvas: #8c8c8c;
    --paper: #ffffff;
    --charcoal: #3b3b3b;
    --ink: #333333;
    --muted: #6a6a6a;
    --lime: #8cc63f;
    --lime-light: #b5dc6e;
    --rule: #cfcfcf;
  }
  * { margin: 0; padding: 0; box-sizing: border-box; }
  html, body { width: 1200px; height: 646px; overflow: hidden; }
  body { background: var(--canvas); font-family: "Open Sans", sans-serif; position: relative; }

  .brand { display: flex; flex-direction: column; align-items: center; }
  .brand-mark { background: var(--lime); }
  .brand-name { font-family: "Montserrat", sans-serif; font-weight: 700; color: var(--lime); letter-spacing: 1px; }

  .letterhead { position: absolute; left: 192px; top: 19px; width: 139px; height: 281px; background: var(--paper); }
  .letterhead .brand { margin-top: 86px; }
  .letterhead .brand-mark { width: 34px; height: 34px; margin-bottom: 8px; }
  .letterhead .brand-name { font-size: 17px; }

  .card-back { position: absolute; left: 132px; top: 367px; width: 269px; height: 173px; background: var(--charcoal); color: #fff; text-align: center; }
  .card-back .brand { margin-top: 26px; }
  .card-back .brand-mark { width: 22px; height: 22px; margin-bottom: 5px; background: #fff; }
  .card-back .brand-name { font-size: 13px; color: #fff; }
  .services { margin-top: 18px; font-size: 8px; line-height: 1.35; }
  .services h3 { font-size: 9px; font-weight: 700; color: var(--lime); }

  .card { position: absolute; width: 314px; height: 183px; background: var(--paper); overflow: hidden; }
  .card .band-top { position: absolute; left: 0; top: 0; width: 314px; height: 24px; }
  .card .band-bottom { position: absolute; left: 0; top: 146px; width: 314px; height: 37px; }
  .card .address { position: absolute; left: 12px; top: 151px; font-size: 10px; font-weight: 700; color: #fff; white-space: nowrap; }
  .card .brand { position: absolute; left: 6px; top: 52px; width: 112px; }
  .card .brand-mark { width: 26px; height: 26px; margin-bottom: 6px; }
  .card .brand-name { font-size: 14px; }
  .card .divider { position: absolute; left: 124px; top: 40px; width: 1px; height: 92px; background: var(--rule); }
  .person { position: absolute; left: 134px; top: 40px; width: 170px; }
  .person .name { font-size: 11px; font-weight: 700; color: var(--ink); white-space: nowrap; }
  .person .role { font-size: 9px; color: var(--muted); margin-bottom: 9px; white-space: nowrap; }
  .contact { list-style: none; font-size: 8px; color: var(--ink); line-height: 14px; }
  .contact li { display: flex; align-items: center; gap: 5px; white-space: nowrap; }
  .contact svg { width: 8px; height: 8px; fill: var(--lime); flex: none; }

  .c1 { left: 475px; top: 149px; }
  .c2 { left: 806px; top: 149px; }
  .c3 { left: 475px; top: 350px; }
  .c4 { left: 806px; top: 350px; }
</style>
</head>
<body>

<section class="letterhead">
  <div class="brand"><span class="brand-mark"></span><span class="brand-name">BRIVOSA</span></div>
</section>

<section class="card-back">
  <div class="brand"><span class="brand-mark"></span><span class="brand-name">BRIVOSA</span></div>
  <div class="services">
    <h3>Our Services:</h3>
    <p>Interior Renovations | Exterior Painting &amp; Carpentry</p>
    <p>Concrete Work | Siding Installation | Step Tread Replacements</p>
  </div>
</section>

<svg width="0" height="0" style="position:absolute">
  <defs>
    <symbol id="i-phone" viewBox="0 0 10 10"><path d="M2 0h2l1 2.5-1.3 1a6 6 0 0 0 2.8 2.8l1-1.3L10 6v2a2 2 0 0 1-2 2A8 8 0 0 1 0 2a2 2 0 0 1 2-2z"/></symbol>
    <symbol id="i-fax" viewBox="0 0 10 10"><path d="M2 0h6v3H2zM0 4h10v4H8v2H2V8H0zM3 7v2h4V7z"/></symbol>
    <symbol id="i-mail" viewBox="0 0 10 10"><path d="M0 2h10v6H0zM1 3l4 3 4-3z"/></symbol>
    <symbol id="i-web" viewBox="0 0 10 10"><circle cx="5" cy="5" r="5"/></symbol>
    <symbol id="band-top" viewBox="0 0 314 24"><rect width="314" height="9" fill="#b5dc6e"/><polygon points="170,0 314,0 314,20 190,20" fill="#8cc63f"/></symbol>
    <symbol id="band-bottom" viewBox="0 0 314 37"><rect width="314" height="26" fill="#3b3b3b"/><polygon points="250,26 314,26 314,37 262,37" fill="#8cc63f"/></symbol>
  </defs>
</svg>

<article class="card c1">
  <svg class="band-top"><use href="#band-top"/></svg>
  <div class="brand"><span class="brand-mark"></span><span class="brand-name">BRIVOSA</span></div>
  <span class="divider"></span>
  <div class="person">
    <p class="name">Derek J. Whitcombe</p>
    <p class="role">President</p>
    <ul class="contact">
      <li><svg><use href="#i-phone"/></svg>615-555-0182</li>
      <li><svg><use href="#i-fax"/></svg>866-555-0147</li>
      <li><svg><use href="#i-mail"/></svg>Dwhitcombe@BrivosaGroup.example</li>
      <li><svg><use href="#i-web"/></svg>www.BrivosaGroup.example</li>
    </ul>
  </div>
  <svg class="band-bottom"><use href="#band-bottom"/></svg>
  <p class="address">1873-K Hollis Bend Rd. #529 Murfreesboro, TN 37190</p>
</article>

<article class="card c2">
  <svg class="band-top"><use href="#band-top"/></svg>
  <div class="brand"><span class="brand-mark"></span><span class="brand-name">BRIVOSA</span></div>
  <span class="divider"></span>
  <div class="person">
    <p class="name">Gideon Hulme</p>
    <p class="role">Administration Manager</p>
    <ul class="contact">
      <li><svg><use href="#i-phone"/></svg>615-555-0164</li>
      <li><svg><use href="#i-fax"/></svg>866-555-0147</li>
      <li><svg><use href="#i-mail"/></svg>GHulme@BrivosaGroup.example</li>
      <li><svg><use href="#i-web"/></svg>www.BrivosaGroup.example</li>
    </ul>
  </div>
  <svg class="band-bottom"><use href="#band-bottom"/></svg>
  <p class="address">1873-K Hollis Bend Rd. #529 Murfreesboro, TN 37190</p>
</article>

<article class="card c3">
  <svg class="band-top"><use href="#band-top"/></svg>
  <div class="brand"><span class="brand-mark"></span><span class="brand-name">BRIVOSA</span></div>
  <span class="divider"></span>
  <div class="person">
    <p class="name">Rolf Tenneker</p>
    <p class="role">Vice-President</p>
    <ul class="contact">
      <li><svg><use href="#i-phone"/></svg>404-555-0139</li>
      <li><svg><use href="#i-fax"/></svg>866-555-0147</li>
      <li><svg><use href="#i-mail"/></svg>RTenneker@BrivosaGroup.example</li>
      <li><svg><use href="#i-web"/></svg>www.BrivosaGroup.example</li>
    </ul>
  </div>
  <svg class="band-bottom"><use href="#band-bottom"/></svg>
  <p class="address">1873-K Hollis Bend Rd. #529 Murfreesboro, TN 37190</p>
</article>

<article class="card c4">
  <svg class="band-top"><use href="#band-top"/></svg>
  <div class="brand"><span class="brand-mark"></span><span class="brand-name">BRIVOSA</span></div>
  <span class="divider"></span>
  <div class="person">
    <p class="name">Oskar Dähn</p>
    <p class="role">Project Manager</p>
    <ul class="contact">
      <li><svg><use href="#i-phone"/></svg>615-555-0121</li>
      <li><svg><use href="#i-fax"/></svg>866-555-0147</li>
      <li><svg><use href="#i-mail"/></svg>ODahn@BrivosaGroup.example</li>
      <li><svg><use href="#i-web"/></svg>www.BrivosaGroup.example</li>
    </ul>
  </div>
  <svg class="band-bottom"><use href="#band-bottom"/></svg>
  <p class="address">1873-K Hollis Bend Rd. #529 Murfreesboro, TN 37190</p>
</article>

</body>
</html>
```